New Web Design Project

Require a website for The Bramwell Harvest. All relevant information is in the uploaded files.

website to be responsive to work on mobile.

Required in html5, css

Coding

Coded - Design and coding required

Number of Pages Required

3 page

```html
<!DOCTYPE html>
<html lang="en">
<head>
<meta charset="utf-8">
<title>The Bramwell Harvest</title>
<meta name="viewport" content="width=device-width, initial-scale=1">
<link href="https://fonts.googleapis.com/css2?family=Oswald:wght@400;500&family=Poppins:wght@300;400;500;600&display=swap" rel="stylesheet">
<style>
:root{
  --orange:#f7941d;
  --green:#8dc63f;
  --ink:#1d1d1d;
  --muted:#8a8a8a;
  --line:#e3e3e3;
  --soft:#f7f7f7;
  --black:#000;
  --white:#fff;
  --tsq:#5b7bc6;
  --chat:#42bdf0;
  --career:#2595d3;
}
*{box-sizing:border-box;margin:0;padding:0}
html,body{width:1200px;height:3098px;overflow:hidden}
body{font-family:"Poppins",sans-serif;color:var(--ink);background:var(--white);position:relative}
a{color:inherit;text-decoration:none}

/* header */
.site-header{position:absolute;top:0;left:0;width:1200px;height:112px;background:var(--white);border-bottom:1px solid #eee}
.brand{position:absolute;left:60px;top:36px;display:flex;align-items:center;gap:8px}
.brand-dot{width:16px;height:16px;border-radius:50%;background:var(--orange)}
.brand-name{font-weight:600;font-size:16px;color:var(--ink);line-height:1.1;width:110px}
.main-nav{position:absolute;left:492px;top:48px;display:flex;gap:0;font-size:11px;letter-spacing:.3px;color:#888}
.main-nav a{margin-right:31px;position:relative}
.main-nav a.active{color:var(--orange)}
.main-nav a.active::after{content:"";position:absolute;left:0;right:0;top:60px;height:3px;background:var(--orange)}
.search-icon{position:absolute;left:922px;top:48px}
.phone-pill{position:absolute;left:968px;top:35px;width:172px;height:44px;border-radius:22px;background:var(--green);color:var(--white);display:flex;align-items:center;padding-left:6px;gap:12px;font-size:17px}
.phone-pill .ring{width:34px;height:34px;border-radius:50%;background:var(--white);display:flex;align-items:center;justify-content:center}

/* hero */
.hero{position:absolute;top:112px;left:0;width:1200px;height:637px;background:linear-gradient(100deg,#4a3b36 0%,#2f2a2a 35%,#23262b 60%,#1a1c20 100%)}
.hero-title{position:absolute;left:61px;top:168px;font-weight:600;font-size:50px;line-height:53px;color:var(--white);letter-spacing:-.3px}
.hero-copy{position:absolute;left:61px;top:340px;width:360px;font-size:12px;line-height:21px;color:#eee}
.btn{display:inline-flex;align-items:center;justify-content:center;background:var(--orange);color:var(--white);border-radius:23px;font-size:13px;font-weight:500}
.hero .btn{position:absolute;left:60px;top:424px;width:120px;height:45px}

/* social strip */
.social-strip{position:absolute;top:749px;left:0;width:1200px;height:45px;display:flex}
.social-strip a{flex:1;display:flex;align-items:center;justify-content:center;gap:8px;color:var(--white);font-size:14px;font-weight:500}
.social-strip .dot{width:10px;height:10px;border-radius:50%;background:var(--white)}
.s-tsq{background:var(--tsq)}.s-chat{background:var(--chat)}.s-career{background:var(--career)}
.s-pic{background:linear-gradient(90deg,#f9d87a,#f59b57,#e2417a,#b540b0,#7b5ee0)}

/* about */
.about{position:absolute;top:794px;left:0;width:1200px;text-align:center}
.about-mark{width:60px;height:60px;border-radius:50%;background:var(--orange);margin:76px auto 0}
.section-title{font-family:"Oswald",sans-serif;font-weight:400;font-size:34px;color:var(--ink)}
.about .section-title{margin-top:34px;line-height:44px}
.about-lead{width:660px;margin:20px auto 0;color:var(--orange);font-size:12.5px;line-height:21px}
.about-text{width:660px;margin:16px auto 0;color:var(--muted);font-size:11px;line-height:19.5px;font-weight:300}
.about-cta{margin-top:14px;font-size:11px;color:#333}
.about-cta a{color:var(--green);text-decoration:underline}

.team-photo{position:absolute;top:1250px;left:0;width:1200px;height:350px;background:linear-gradient(180deg,#ffffff 0%,#ece6df 40%,#d9cfc3 100%)}

/* founders */
.founders{position:absolute;top:1600px;left:0;width:1200px;height:546px}
.founders .divider{position:absolute;left:600px;top:77px;width:1px;height:391px;background:var(--line)}
.founder{position:absolute;top:70px;width:400px;text-align:center}
.founder.left{left:137px}.founder.right{left:663px}
.founder .section-title{font-size:33px;line-height:44px}
.founder .role{font-size:15px;margin-top:4px}
.founder.left .role{color:var(--orange)}.founder.right .role{color:var(--green)}
.avatar{width:134px;height:134px;border-radius:50%;margin:18px auto 0;border:5px solid var(--green);background:linear-gradient(160deg,#7d7a76,#2f3540)}
.founder.right .avatar{border-color:var(--orange);background:linear-gradient(160deg,#e8e2da,#2b2b30)}
.founder .bio{margin-top:22px;font-size:11px;line-height:19px;color:var(--muted);font-weight:300}
.founder .url{margin-top:19px;font-size:13px;letter-spacing:.4px;color:#222}
.founder .more{display:inline-flex;align-items:center;gap:7px;margin-top:17px;font-size:12px}
.founder.left .more{color:var(--green)}.founder.right .more{color:var(--orange)}

/* contact */
.contact-band{position:absolute;top:2146px;left:0;width:1200px;height:395px;background:var(--soft)}
.footer{position:absolute;top:2541px;left:0;width:1200px;height:557px;background:var(--black);color:var(--white)}
.contact-card{position:absolute;top:2220px;left:319px;width:562px;height:396px;background:var(--white);text-align:center}
.contact-card h2{margin-top:36px;font-weight:600;font-size:29px;letter-spacing:1px;color:#111}
.contact-card p{width:400px;margin:14px auto 0;font-size:11px;line-height:19px;color:var(--muted);font-weight:300}
.field{position:absolute;border:1px solid var(--line);font-size:11px;color:#555;padding:12px}
.f-name{left:48px;top:150px;width:225px;height:44px}
.f-email{left:288px;top:150px;width:225px;height:44px}
.f-msg{left:48px;top:210px;width:465px;height:89px}
.contact-card .btn{position:absolute;left:228px;top:315px;width:106px;height:44px}

/* footer */
.footer-brand{position:absolute;top:160px;left:0;width:1200px;display:flex;justify-content:center;align-items:center;gap:10px}
.footer-brand .brand-dot{width:18px;height:18px}
.footer-brand .brand-name{color:var(--white);font-size:24px;width:auto}
.footer-contact{position:absolute;top:278px;left:0;width:1200px;display:flex;justify-content:center;align-items:center;gap:12px;font-size:12px}
.footer-contact .sep{margin:0 12px}
.footer-nav{position:absolute;top:322px;left:0;width:1200px;text-align:center;font-size:12.5px;color:#ddd}
.footer-nav span{margin:0 10px}
.footer-social{position:absolute;top:368px;left:0;width:1200px;display:flex;justify-content:center;gap:7px}
.footer-social a{width:38px;height:38px;border-radius:50%}
.footer-rule{position:absolute;top:481px;left:60px;width:908px;height:1px;background:#444}
.copyright{position:absolute;top:510px;left:0;width:1200px;text-align:center;font-size:11px;color:#bbb}
</style>
</head>
<body>

<header class="site-header">
  <a class="brand" href="#"><span class="brand-dot"></span><span class="brand-name">The Bramwell Harvest</span></a>
  <nav class="main-nav">
    <a class="active" href="#">HOME</a><a href="#">ABOUT</a><a href="#">PEOPLE</a><a href="#">SOCIAL MEDIA LINKS</a><a href="#">CONTACT</a>
  </nav>
  <svg class="search-icon" width="16" height="16" viewBox="0 0 16 16" fill="none" stroke="#444" stroke-width="1.6"><circle cx="6.5" cy="6.5" r="5"/><line x1="10.3" y1="10.3" x2="15" y2="15"/></svg>
  <a class="phone-pill" href="#"><span class="ring"><svg width="18" height="18" viewBox="0 0 24 24" fill="#f7941d"><path d="M6.6 10.8a15 15 0 006.6 6.6l2.2-2.2a1 1 0 011-.25 11.4 11.4 0 003.6.6 1 1 0 011 1V20a1 1 0 01-1 1A17 17 0 013 4a1 1 0 011-1h3.5a1 1 0 011 1c0 1.25.2 2.45.6 3.6a1 1 0 01-.25 1z"/></svg></span>555.014.2288</a>
</header>

<section class="hero" role="img" aria-label="Evening city skyline with a busy avenue of traffic below">
  <h1 class="hero-title">So You Can<br>Focus On Your<br>Business</h1>
  <p class="hero-copy">Lorem ipsum dolor sit amet, consectetur adipiscing elit, sed Duis aute irure dolor in reprehenderit in voluptate velit esse cillum dolore eu fugiat nulla pariatur.</p>
  <a class="btn" href="#">LEARN MORE</a>
</section>

<nav class="social-strip">
  <a class="s-tsq" href="#"><span class="dot"></span>Townsquare</a>
  <a class="s-chat" href="#"><span class="dot"></span>Chatter</a>
  <a class="s-career" href="#"><span class="dot"></span>Careerlink</a>
  <a class="s-pic" href="#"><span class="dot"></span>Pictorial</a>
</nav>

<section class="about">
  <div class="about-mark"></div>
  <h2 class="section-title">About The Bramwell Harvest Company</h2>
  <p class="about-lead">The Bramwell Harvest Company was incorporated with the objective of introducing new vendors to the Canadian market through a trusted and mutual business relation</p>
  <p class="about-text">It was set up by Ravi Castellan and Theo Marchetti who have a combined experience of over 45 years in the fresh produce business. With Ravi's expertise in global sourcing and Theo's vast connection and know how of the Canadian market, we have helped our existing partners grow and expand their reach in the Canadian fresh produce market.</p>
  <p class="about-text">Our expertise and supply chain knowledge allow us to develop programs and introduce new products to the Canadian consumer, via retail and wholesale channels across Canada.</p>
  <p class="about-cta"><a href="#">Get in touch</a> to discuss how we can add value to your business</p>
</section>

<div class="team-photo" role="img" aria-label="A row of diverse people standing with laptops, tablets and phones"></div>

<section class="founders">
  <div class="founder left">
    <h2 class="section-title">Theo Marchetti</h2>
    <p class="role">Founder</p>
    <div class="avatar" role="img" aria-label="Portrait of Theo Marchetti"></div>
    <p class="bio">Lorem ipsum dolor sit amet, consectetur adipiscing elit, sed do eiusmod tempor incididunt ut labore et dolore magna aliqua. Ut enim ad minim veniam, quis nostrud exercitation ullamco laboris nisi ut aliquip.</p>
    <p class="url">https://www.profilehub.example/in/theo-marchetti-41bc207/</p>
    <a class="more" href="#">LEARN MORE <svg width="9" height="10" viewBox="0 0 9 10"><path d="M0 0l9 5-9 5z" fill="currentColor"/></svg></a>
  </div>
  <div class="divider"></div>
  <div class="founder right">
    <h2 class="section-title">Ravi Castellan</h2>
    <p class="role">Founder &amp; President</p>
    <div class="avatar" role="img" aria-label="Portrait of Ravi Castellan"></div>
    <p class="bio">Lorem ipsum dolor sit amet, consectetur adipiscing elit, sed do eiusmod tempor incididunt ut labore et dolore magna aliqua. Ut enim ad minim veniam, quis nostrud exercitation ullamco laboris nisi ut aliquip.</p>
    <p class="url">https://www.profilehub.example/in/ravi-castellan-52de318/</p>
    <a class="more" href="#">LEARN MORE <svg width="9" height="10" viewBox="0 0 9 10"><path d="M0 0l9 5-9 5z" fill="currentColor"/></svg></a>
  </div>
</section>

<div class="contact-band"></div>

<footer class="footer">
  <div class="footer-brand"><span class="brand-dot"></span><span class="brand-name">The Bramwell Harvest</span></div>
  <div class="footer-contact">
    <svg width="12" height="15" viewBox="0 0 12 15"><path d="M6 0a6 6 0 016 6c0 4-6 9-6 9S0 10 0 6a6 6 0 016-6z" fill="#f7941d"/><circle cx="6" cy="6" r="2.2" fill="#000"/></svg>
    <span>123, Address,Street,State,City, Zipcode</span><span class="sep">|</span>
    <svg width="16" height="11" viewBox="0 0 16 11"><rect width="16" height="11" fill="#f7941d"/><path d="M0 0l8 6 8-6" stroke="#000" stroke-width="1.2" fill="none"/></svg>
    <span>hello@bramwellharvest.example</span><span class="sep">|</span>
    <svg width="15" height="15" viewBox="0 0 24 24" fill="#f7941d"><path d="M6.6 10.8a15 15 0 006.6 6.6l2.2-2.2a1 1 0 011-.25 11.4 11.4 0 003.6.6 1 1 0 011 1V20a1 1 0 01-1 1A17 17 0 013 4a1 1 0 011-1h3.5a1 1 0 011 1c0 1.25.2 2.45.6 3.6a1 1 0 01-.25 1z"/></svg>
    <span>555.014.2288</span>
  </div>
  <nav class="footer-nav"><a href="#">Home</a><span>|</span><a href="#">About</a><span>|</span><a href="#">People</a><span>|</span><a href="#">Social Media Links</a><span>|</span><a href="#">Contact</a></nav>
  <div class="footer-social">
    <a href="#" class="s-tsq" aria-label="Townsquare"></a>
    <a href="#" class="s-chat" aria-label="Chatter"></a>
    <a href="#" class="s-career" aria-label="Careerlink"></a>
    <a href="#" class="s-pic" aria-label="Pictorial"></a>
  </div>
  <div class="footer-rule"></div>
  <p class="copyright">Copyright © 2020 The Bramwell Harvest Company . &nbsp; All rights reserved.</p>
</footer>

<section class="contact-card">
  <h2>CONTACT US</h2>
  <p>Lorem ipsum dolor sit amet, consectetur adipiscing elit, sed do eiusmod tempor incididunt ut labore et dolore magna aliqua.</p>
  <div class="field f-name">Your Name</div>
  <div class="field f-email">Your Email</div>
  <div class="field f-msg">Message / Comments :</div>
  <a class="btn" href="#">SEND</a>
</section>

</body>
</html>
```